Local Finance and Insurance Advising Company from Switzerland needs an impressive banner design.

I am looking for an impressive Banner Design, I need this Banner for Facebook, LinkedIn, YouTube & Google.

I am Advising all kind of peoples who are living here in Switzerland. Young, middle age and old people. People who want to go study, people who are planning to create a family, old people who are, or going to retire. Expatriates who want to leave Switzerland to live in another country, expatriates who are coming to Switzerland. Peoples who ant to build their own business up. All kind of financial, insurance and pension planning's.

The Company Name is: Alpine Counsel
Our slogen / heading is: Clear Guidance, no Pitch

The Company logo can be used for the banner, but I would preffer to have the banner without logo, as the logo will be already in a another field on the social networks.

Since the first impression is the most important, this project is really important to me. I am ready to realize further projects with the one who can create the perfect banner who hits the point as described. I am a start-up company, everything is still on beginning and still much has to be done.

Target Market(s)

private clients

Requirements
Must have
• The banner should give the impression of happiness, safeness, health and freedom. Empowering people and creating freedom lifestyles.
Should not have
• I do not want that the banner looks like we are some kind of broker who is just selling some kind of insurances.

```html
<!DOCTYPE html>
<html lang="en">
<head>
<meta charset="utf-8">
<title>Alpine Counsel – Banner</title>
<link href="https://fonts.googleapis.com/css2?family=Fira+Sans:ital,wght@0,700;1,400;1,700&display=swap" rel="stylesheet">
<style>
  :root {
    --page-bg: #f1f1f2;
    --panel-grey: #d9d9db;
    --band-grey: #e9e9eb;
    --brand-red: #e3131b;
    --deep-red: #c40f16;
    --soft-red: #e2545a;
    --white: #ffffff;
  }
  html, body {
    margin: 0;
    width: 1200px;
    height: 671px;
    overflow: hidden;
    background: var(--page-bg);
  }
  .banner {
    position: absolute;
    left: 0;
    top: 80px;
    width: 1200px;
    height: 512px;
    overflow: hidden;
    background: var(--panel-grey);
  }
  .banner__shapes {
    position: absolute;
    inset: 0;
  }
  .brand-name {
    position: absolute;
    left: 79px;
    top: 76px;
    margin: 0;
    font-family: "Fira Sans", sans-serif;
    font-weight: 700;
    font-size: 26px;
    letter-spacing: 0.5px;
    color: var(--brand-red);
  }
  .headline {
    position: absolute;
    left: 257px;
    top: 300px;
    margin: 0;
    font-family: "Fira Sans", sans-serif;
    font-style: italic;
    color: var(--white);
    font-size: 52px;
    line-height: 64px;
  }
  .headline__lead {
    display: block;
    font-weight: 700;
    letter-spacing: -1px;
  }
  .headline__tail {
    display: block;
    font-weight: 400;
  }
</style>
</head>
<body>
  <section class="banner">
    <svg class="banner__shapes" width="1200" height="512" viewBox="0 0 1200 512" xmlns="http://www.w3.org/2000/svg">
      <defs>
        <linearGradient id="waveFill" x1="0" y1="0" x2="1" y2="0">
          <stop offset="0" stop-color="var(--soft-red)"/>
          <stop offset="0.55" stop-color="var(--brand-red)"/>
          <stop offset="1" stop-color="var(--deep-red)"/>
        </linearGradient>
        <linearGradient id="photoFill" x1="0" y1="0" x2="1" y2="1">
          <stop offset="0" stop-color="#d9c7b4"/>
          <stop offset="0.5" stop-color="#c99f86"/>
          <stop offset="1" stop-color="#7fa9c9"/>
        </linearGradient>
      </defs>

      <path class="light-band" fill="var(--band-grey)"
            d="M0,268 C80,290 180,300 280,210 C380,120 480,40 600,40 C700,40 760,90 780,200 L858,512 L0,512 Z"/>

      <g role="img" aria-label="Faint mountain landscape with a flag on the summit, tinted red">
        <path class="red-wave" fill="url(#waveFill)"
              d="M0,322 C80,345 180,350 280,260 C380,170 480,88 586,88 C680,88 700,150 705,230 C710,330 760,440 858,512 L0,512 Z"/>
      </g>

      <path class="top-accent" fill="var(--brand-red)"
            d="M563,0 C620,22 680,40 740,35 C790,30 810,12 835,0 Z"/>
      <path class="corner-accent" fill="var(--brand-red)"
            d="M1069,0 L1200,0 L1200,133 C1170,80 1120,30 1069,0 Z"/>

      <circle class="photo-ring" cx="960" cy="254" r="244" fill="var(--band-grey)"/>
      <circle class="family-photo" cx="960" cy="254" r="219" fill="url(#photoFill)"
              role="img" aria-label="Smiling three-generation family: grandparents, parents and two children hugging"/>
    </svg>

    <p class="brand-name">Alpine Counsel</p>

    <h1 class="headline">
      <span class="headline__lead">Clear Guidance,</span>
      <span class="headline__tail">no Pitch</span>
    </h1>
  </section>
</body>
</html>
```